Cloud Based Internet Protection Service Business Cards

I would like a professionally designed business card. I already have a logo which I have attached.

The business is an online cloud based internet protection service aimed parents, particularly at non-technical parents and also schools.

The card should be be quite simple in its design, not to full of text and give its information in a clear and concise manner

Target Market(s)

Parents (especially non-technical parents) and also schools

Industry/Entity Type

Internet

Colors

Designer to choose colors to be used in the design.

Requirements
Should not have
• Too much text or be too cluttered. No decorative fonts, just a clear and concise font.

```html
<!DOCTYPE html>
<html lang="en">
<head>
<meta charset="utf-8">
<title>Safenest Business Card</title>
<link href="https://fonts.googleapis.com/css2?family=Exo+2:wght@400;500;600&display=swap" rel="stylesheet">
<style>
  :root {
    --navy: #0f3f5f;
    --navy-deep: #0c3552;
    --sky: #2aa0d8;
    --white: #ffffff;
    --paper: #fbfbfb;
    --stage: #e6e6e6;
    --text-light: #e8f1f6;
  }
  * { margin: 0; padding: 0; box-sizing: border-box; }
  html, body { width: 800px; height: 1200px; overflow: hidden; }
  body {
    background: var(--stage);
    font-family: "Exo 2", sans-serif;
    position: relative;
  }
  .card {
    position: absolute;
    top: 322px;
    width: 320px;
    height: 556px;
    border-radius: 16px;
    overflow: hidden;
    box-shadow: 0 6px 14px rgba(0,0,0,0.28);
  }
  .card-front { left: 70px; background: var(--paper); }
  .card-back { left: 410px; background: var(--navy); color: var(--text-light); }

  .emblem-area {
    position: absolute;
    top: 58px;
    left: 0;
    width: 320px;
    height: 276px;
    background: linear-gradient(160deg, var(--navy-deep) 0%, var(--navy) 45%, var(--sky) 100%);
    opacity: 0.9;
  }

  .wordmark {
    position: absolute;
    left: 0; right: 0;
    display: flex;
    align-items: center;
    justify-content: center;
    gap: 8px;
    font-weight: 600;
    letter-spacing: 2px;
  }
  .wordmark-dot { width: 14px; height: 14px; border-radius: 50%; background: var(--sky); }
  .card-front .wordmark { top: 428px; font-size: 34px; color: var(--navy); }
  .card-back .wordmark { top: 82px; font-size: 30px; color: var(--white); }

  .person { position: absolute; top: 212px; left: 0; right: 0; text-align: center; }
  .person-name { font-size: 20px; font-weight: 500; color: var(--white); }
  .person-title { font-size: 17px; color: var(--sky); margin-top: 2px; }

  .contact { position: absolute; top: 372px; left: 0; right: 0; text-align: center; font-size: 14px; line-height: 18px; }
  .contact-phones { margin-top: 16px; display: inline-flex; flex-direction: column; gap: 1px; }
  .phone-line { display: flex; align-items: center; gap: 6px; }
  .phone-icon { width: 13px; height: 13px; }
  .contact-email { margin-top: 12px; }

  .web-band { position: absolute; left: 0; bottom: 0; width: 320px; height: 44px; }
  .web-address {
    position: absolute; left: 0; right: 0; bottom: 8px;
    text-align: center; font-size: 14px; color: var(--white);
  }
</style>
</head>
<body>
  <div class="card card-front">
    <div class="emblem-area" role="img" aria-label="Brand emblem: shield with a family inside, wrapped by a cloud swirl"></div>
    <div class="wordmark"><span class="wordmark-dot"></span>SAFENEST</div>
  </div>

  <div class="card card-back">
    <div class="wordmark"><span class="wordmark-dot"></span>SAFENEST</div>

    <div class="person">
      <div class="person-name">Martin Hale</div>
      <div class="person-title">President</div>
    </div>

    <div class="contact">
      <div>Street Address, Somewhere</div>
      <div>Cityname, State 00000</div>
      <div class="contact-phones">
        <div class="phone-line">
          <svg class="phone-icon" viewBox="0 0 14 14"><circle cx="7" cy="7" r="7" fill="#2aa0d8"/><path d="M4.6 3.6l1.3 1.5-.7 1a5 5 0 0 0 2.7 2.7l1-.7 1.5 1.3-.9 1.1C6.7 10.3 3.7 7.3 3.5 4.5z" fill="#fff"/></svg>
          <span>+00 000.000.000</span>
        </div>
        <div class="phone-line">
          <svg class="phone-icon" viewBox="0 0 14 14"><circle cx="7" cy="7" r="7" fill="#2aa0d8"/><rect x="5" y="3" width="4" height="8" rx="0.8" fill="#fff"/><rect x="5.8" y="4" width="2.4" height="5" fill="#2aa0d8"/></svg>
          <span>+00 000.000.000</span>
        </div>
      </div>
      <div class="contact-email">martin@safenest.com</div>
    </div>

    <svg class="web-band" viewBox="0 0 320 44" preserveAspectRatio="none">
      <path d="M0 12 Q160 -8 320 12 L320 44 L0 44 Z" fill="#2aa0d8"/>
    </svg>
    <div class="web-address">www.safenest.com</div>
  </div>
</body>
</html>
```